Graphic Insert - For Pillow Case

We are purchasing new pillow cases for a campaign we are running and need a graphic insert as part of our corporate branding and product description to go in our packaging. The packaging will be a clear plastic back with this graphic insert.

Size of Flyer: 6"x9"

Description: 440 Thread Count Egyptian Cotton Pillow Cases
Quantity: 2
Size of Pillow Case: Standard
Descriptive Words: Soft, Caress, Smooth, Gentle

Our website: www.velardo.com

Thanks,

Dale

```html
<!DOCTYPE html>
<html lang="en">
<head>
<meta charset="utf-8">
<title>Velardo Pillow Case Insert Designs</title>
<link href="https://fonts.googleapis.com/css2?family=Arimo:wght@400;700&display=swap" rel="stylesheet">
<style>
  :root {
    --page: #ffffff;
    --ink-black: #000000;
    --ink-grey: #666663;
    --paper-white: #ffffff;
    --paper-linen: #e3e1d6;
    --logo-grey: #6b6b6b;
    --shadow: rgba(0,0,0,0.35);
  }
  html, body {
    margin: 0;
    padding: 0;
    width: 1200px;
    height: 900px;
    overflow: hidden;
    background: var(--page);
    font-family: "Arimo", Arial, sans-serif;
  }
  .sheet { position: relative; width: 1200px; height: 900px; }

  .insert {
    position: absolute;
    top: 236px;
    width: 256px;
    height: 384px;
    box-sizing: border-box;
    border: 8px solid var(--frame);
    background: var(--paper);
    color: var(--ink);
    box-shadow: 4px 5px 6px var(--shadow);
  }
  .insert--black { --frame: var(--ink-black); --ink: var(--ink-black); --badge: var(--ink-black); }
  .insert--grey  { --frame: var(--ink-grey);  --ink: var(--ink-grey);  --badge: var(--ink-grey); }
  .insert--white { --paper: var(--paper-white); }
  .insert--linen { --paper: var(--paper-linen); }

  .brand {
    position: absolute;
    left: 34px;
    top: 35px;
    display: flex;
    align-items: center;
    gap: 10px;
  }
  .brand__mark {
    width: 48px;
    height: 48px;
    border: 2px solid var(--logo-grey);
    border-radius: 50%;
  }
  .brand__name {
    font-size: 24px;
    font-weight: 400;
    letter-spacing: 3px;
    color: var(--logo-grey);
  }

  .rule {
    position: absolute;
    left: 35px;
    width: 170px;
    height: 3px;
    background: var(--ink);
  }
  .rule--top { top: 109px; }
  .rule--bottom { top: 203px; }

  .product-title {
    position: absolute;
    left: 35px;
    top: 122px;
    margin: 0;
    font-size: 18.5px;
    line-height: 23.5px;
    font-weight: 700;
  }
  .product-size {
    position: absolute;
    left: 35px;
    top: 225px;
    margin: 0;
    font-size: 12.5px;
    font-weight: 700;
  }
  .product-words {
    position: absolute;
    left: 35px;
    top: 251px;
    margin: 0;
    font-size: 10.5px;
    font-weight: 700;
  }
  .website {
    position: absolute;
    left: 35px;
    top: 318px;
    margin: 0;
    font-size: 10.5px;
    font-weight: 400;
  }
  .quantity-badge {
    position: absolute;
    left: 150px;
    top: 275px;
    width: 53px;
    height: 53px;
    border-radius: 50%;
    background: var(--badge);
    color: #ffffff;
    display: flex;
    align-items: baseline;
    justify-content: center;
    padding-top: 10px;
    box-sizing: border-box;
  }
  .quantity-badge__number { font-size: 27px; font-weight: 700; line-height: 1; }
  .quantity-badge__unit { font-size: 10px; font-weight: 400; }

  .caption {
    position: absolute;
    top: 632px;
    margin: 0;
    font-size: 14px;
    color: var(--ink-black);
    white-space: nowrap;
  }
  .caption strong { font-weight: 700; }
</style>
</head>
<body>
<main class="sheet">

  <section class="insert insert--black insert--white" style="left:47px">
    <div class="brand"><span class="brand__mark"></span><span class="brand__name">VELARDO</span></div>
    <div class="rule rule--top"></div>
    <h2 class="product-title">440 Thread Count<br>Egyptian Cotton<br>Pillow Cases</h2>
    <div class="rule rule--bottom"></div>
    <p class="product-size">Standard Size</p>
    <p class="product-words">Soft, Caress, Smooth, Gentle</p>
    <p class="website">www.velardo.com</p>
    <div class="quantity-badge"><span class="quantity-badge__number">2</span><span class="quantity-badge__unit">pcs</span></div>
  </section>
  <p class="caption" style="left:59px"><strong>Design 01.1:</strong> Pillow Case Flyer Design</p>

  <section class="insert insert--grey insert--white" style="left:330px">
    <div class="brand"><span class="brand__mark"></span><span class="brand__name">VELARDO</span></div>
    <div class="rule rule--top"></div>
    <h2 class="product-title">440 Thread Count<br>Egyptian Cotton<br>Pillow Cases</h2>
    <div class="rule rule--bottom"></div>
    <p class="product-size">Standard Size</p>
    <p class="product-words">Soft, Caress, Smooth, Gentle</p>
    <p class="website">www.velardo.com</p>
    <div class="quantity-badge"><span class="quantity-badge__number">2</span><span class="quantity-badge__unit">pcs</span></div>
  </section>
  <p class="caption" style="left:342px"><strong>Design 01.2:</strong> Pillow Case Flyer Design</p>

  <section class="insert insert--black insert--linen" style="left:614px">
    <div class="brand"><span class="brand__mark"></span><span class="brand__name">VELARDO</span></div>
    <div class="rule rule--top"></div>
    <h2 class="product-title">440 Thread Count<br>Egyptian Cotton<br>Pillow Cases</h2>
    <div class="rule rule--bottom"></div>
    <p class="product-size">Standard Size</p>
    <p class="product-words">Soft, Caress, Smooth, Gentle</p>
    <p class="website">www.velardo.com</p>
    <div class="quantity-badge"><span class="quantity-badge__number">2</span><span class="quantity-badge__unit">pcs</span></div>
  </section>
  <p class="caption" style="left:626px"><strong>Design 01.3:</strong> Pillow Case Flyer Design</p>

  <section class="insert insert--grey insert--linen" style="left:897px">
    <div class="brand"><span class="brand__mark"></span><span class="brand__name">VELARDO</span></div>
    <div class="rule rule--top"></div>
    <h2 class="product-title">440 Thread Count<br>Egyptian Cotton<br>Pillow Cases</h2>
    <div class="rule rule--bottom"></div>
    <p class="product-size">Standard Size</p>
    <p class="product-words">Soft, Caress, Smooth, Gentle</p>
    <p class="website">www.velardo.com</p>
    <div class="quantity-badge"><span class="quantity-badge__number">2</span><span class="quantity-badge__unit">pcs</span></div>
  </section>
  <p class="caption" style="left:909px"><strong>Design 01.4:</strong> Pillow Case Flyer Design</p>

</main>
</body>
</html>
```